creation of business cards for Velanto Sàrl

Velanto S% 26 # 224; rl is a soci% 26 # 233; t% 26 # 233; consultancy that accompanies companies in the development of their business on the market% 26 # 233; Switzerland by providing strategic contacts or market information; and by providing administrative or logistical support. Our consulting skills focus on sectors% 26 # 224; high value added% 26 # 233; e, such as trade in food goods% 26 # 39amp; drinks, fashion% 26amp; lifestyle, products and services for% 26 # 233; s in high-tech industries (pharmaceutical, chemical, m% 26 # 233; pricy 26% 23 #; cision) or sustainable solutions (% 26 # 233; energies renewable, mat% 26 # 233; recyclable materials). As part of the launch of our activity% 26 # 233;, we need% 26 # 39;% 26 # 233; to establish business cards to d% 26 # 233; work our new customers (Swiss or international).

Target Market(s)

Companies wishing to develop their activity% 26 # 233; s in Switzerland or% 26 # 224; l% 26 # 39;% 26 # 233; abroad (mainly in Europe).

Contact Information for Business Card

Prénom NOM
Velanto Sàrl
Bureau de Marvoisin
Rue des Tilleuls 47, 2000 Neuchâtel
Tél. : 032 718 46 39
info@velanto-example.ch
www.velanto-example.ch

Font styles to use
Serif
Sans Serif

Colors

Designer to choose colors to be used in the design.

Requirements
Must have
• The logo The name of the company% 26 # 233; t% 26 # 233; (Velanto S% 26 # 224; rl) One field for the mailing address One field for the number% 26 # 233; ro de t% 26 # 233; l% 26 # 233; phone One field for the % 26 # 39; email address and website

```html
<!DOCTYPE html>
<html lang="fr">
<head>
<meta charset="utf-8">
<title>Velanto Sàrl – cartes de visite</title>
<link rel="stylesheet" href="https://fonts.googleapis.com/css2?family=Lato:ital,wght@0,300;0,400;0,700;1,400&display=swap">
<style>
  :root {
    --teal-deep: #023d51;
    --teal-soft: #3e6b7d;
    --paper: #f4f4f4;
    --paper-shade: #e6e6e6;
    --ink: #222b30;
    --ink-muted: #4a5257;
    --rule: #8aa0ad;
    --backdrop: #cbcbcb;
    --mark-light: #eef1f2;
  }
  * { box-sizing: border-box; margin: 0; padding: 0; }
  html, body {
    width: 1200px; height: 675px; overflow: hidden;
    background: var(--backdrop);
    font-family: "Lato", sans-serif;
  }
  .sheet {
    width: 1200px; height: 675px;
    display: flex; align-items: center; justify-content: center; gap: 40px;
  }
  .card {
    position: relative;
    width: 520px; height: 336px;
    border-radius: 18px;
    overflow: hidden;
  }

  /* Front */
  .card--front {
    background: var(--teal-deep);
    display: flex; align-items: center; justify-content: center;
  }
  .brand { display: flex; align-items: center; gap: 16px; }
  .brand__square {
    width: 46px; height: 46px; border-radius: 10px;
    background: var(--mark-light);
  }
  .brand__name {
    font-weight: 300; font-size: 40px; letter-spacing: 4px;
    color: var(--mark-light);
  }

  /* Back */
  .card--back {
    background: linear-gradient(135deg, var(--paper-shade) 0%, var(--paper) 45%, #ffffff 100%);
  }
  .card--back .brand {
    position: absolute; left: 34px; top: 118px; gap: 13px;
  }
  .card--back .brand__square {
    width: 34px; height: 34px; border-radius: 8px; background: var(--teal-deep);
  }
  .card--back .brand__name {
    font-size: 29px; letter-spacing: 3px; color: var(--teal-deep);
  }
  .divider {
    position: absolute; left: 262px; top: 92px;
    width: 1.5px; height: 152px; background: var(--rule);
  }
  .contact {
    position: absolute; left: 284px; top: 88px;
    color: var(--ink); font-size: 12.5px; line-height: 1.45;
  }
  .contact__name {
    font-weight: 700; font-size: 17px; color: var(--teal-deep); line-height: 1.2;
  }
  .contact__company { color: var(--ink-muted); margin-bottom: 8px; }
  .contact__address { margin-bottom: 8px; }
  .contact__line { display: flex; align-items: center; gap: 8px; }
  .contact__line svg { width: 11px; height: 11px; flex: none; }
  .band {
    position: absolute; left: 0; bottom: 0; width: 520px; height: 14px;
  }
</style>
</head>
<body>
<main class="sheet">
  <section class="card card--front" aria-label="Recto">
    <div class="brand">
      <span class="brand__square"></span>
      <span class="brand__name">VELANTO</span>
    </div>
  </section>

  <section class="card card--back" aria-label="Verso">
    <div class="brand">
      <span class="brand__square"></span>
      <span class="brand__name">VELANTO</span>
    </div>
    <span class="divider"></span>
    <div class="contact">
      <p class="contact__name">Prénom NOM</p>
      <p class="contact__company">Velanto Sàrl</p>
      <p class="contact__address">Bureau de Marvoisin<br>Rue des Tilleuls 47, 2000 Neuchâtel</p>
      <p class="contact__line">
        <svg viewBox="0 0 12 12" aria-hidden="true"><path fill="#023d51" d="M2.6 0.6l1.8 2.3-1 1.2c.7 1.6 2 2.9 3.6 3.6l1.2-1 2.3 1.8-.9 2.2C5 10.6 1.4 7 .5 1.5z"/></svg>
        032 718 46 39
      </p>
      <p class="contact__line">
        <svg viewBox="0 0 12 12" aria-hidden="true"><rect x="0.5" y="2" width="11" height="8" fill="#023d51"/><path d="M0.8 2.4L6 6.6l5.2-4.2" stroke="#fff" stroke-width="1" fill="none"/></svg>
        info@velanto-example.ch
      </p>
      <p class="contact__line">
        <svg viewBox="0 0 12 12" aria-hidden="true"><g fill="none" stroke="#023d51" stroke-width="1"><circle cx="6" cy="6" r="5.2"/><ellipse cx="6" cy="6" rx="2.2" ry="5.2"/><path d="M0.8 6h10.4M1.6 3.4h8.8M1.6 8.6h8.8"/></g></svg>
        www.velanto-example.ch
      </p>
    </div>
    <svg class="band" viewBox="0 0 520 14" preserveAspectRatio="none" aria-hidden="true">
      <polygon points="0,0 218,0 206,14 0,14" fill="#023d51"/>
      <polygon points="226,0 520,0 520,14 214,14" fill="#3e6b7d"/>
    </svg>
  </section>
</main>
</body>
</html>
```